New more attractive design for an old tired look that is high tech but inviting

Need a more modern eye catching design. We are and I/T and MSP and we need a new look. Need a call to action on each page. Needs to be in WordPress. Existing site is brivanoqe.com. Needs to work on phones and tablets. The default home page should present us as an MSP/MSSP and direct the viewer to our services we offer.
Updates

Current deadline assigned at project inception has passed before project started

Need extra days to review

Target Market(s)

Our target market is other businesses. We do not target residential customers.

Industry/Entity Type

Business to Business oriented

Coding

Coded - Design and coding required

Number of Pages Required

5+ page

Font styles to use
Sans Serif

Requirements
Must have
• Must have a current relevant design with a call to action on each page.
Nice to have
• Dark background high tech look with people to make it attractive

```html
<!DOCTYPE html>
<html lang="en">
<head>
<meta charset="utf-8">
<title>Brivano Systems – Data Center Services</title>
<link href="https://fonts.googleapis.com/css2?family=Poppins:wght@300;400;500;600;700&display=swap" rel="stylesheet">
<style>
:root{
  --red:#c8262f;
  --navy:#2c3e4c;
  --ink:#1c1f24;
  --heading:#33414d;
  --text:#5a6068;
  --light-bg:#e9edf0;
  --card-border:#f0c9cd;
  --white:#ffffff;
}
*{box-sizing:border-box;margin:0;padding:0}
html,body{width:1200px;height:2955px;overflow:hidden}
body{font-family:"Poppins",sans-serif;color:var(--ink);background:var(--white);position:relative}

/* header */
.site-header{position:absolute;left:0;top:0;width:1200px;height:82px;background:rgba(10,14,22,.75);z-index:3}
.brand{position:absolute;left:60px;top:18px;display:flex;align-items:center;gap:10px;color:var(--white);font-weight:600;font-size:26px;letter-spacing:-.3px}
.brand-mark{width:12px;height:12px;background:var(--red)}
.main-nav{position:absolute;left:568px;top:34px;display:flex;gap:33px;font-size:15px;color:var(--white)}
.main-nav a{color:var(--white);text-decoration:none;position:relative}
.main-nav a.active::after{content:"";position:absolute;left:0;right:0;bottom:-32px;height:2px;background:var(--red)}
.call-btn{position:absolute;display:flex;align-items:center;gap:14px;background:var(--red);color:var(--white);font-weight:600;font-size:15px;letter-spacing:1px;padding:0 16px;height:40px}
.call-btn::after{content:"";position:absolute;right:-14px;top:0;width:7px;height:100%;background:var(--red)}

/* hero */
.hero{position:absolute;left:0;top:0;width:1200px;height:675px;background:radial-gradient(ellipse at 78% 40%,#3b5b7e 0%,#1c3150 35%,#0c1729 75%)}
.hero-title{position:absolute;left:57px;top:235px;color:var(--white);font-weight:700;font-size:58px;line-height:1}
.hero-sub{position:absolute;left:205px;top:310px;color:var(--white);font-weight:300;font-size:58px;line-height:1}
.hero-rule{position:absolute;left:60px;top:307px;width:238px;height:2px;background:var(--red)}
.hero-text{position:absolute;left:61px;top:388px;width:460px;color:var(--white);font-size:14px;line-height:23px}

/* why */
.section-title{position:absolute;width:1200px;text-align:center;color:var(--heading);font-weight:600;font-size:28px}
.feature{position:absolute;width:227px;height:227px;border:1px solid var(--card-border);background:var(--white);text-align:center;padding:30px 18px 0}
.feature h3{font-size:18px;font-weight:600;margin:10px 0 6px;color:var(--ink)}
.feature p{font-size:12.5px;line-height:19.5px;color:var(--text)}
.link-line{position:absolute;height:2px;background:var(--red);top:974px}

/* about */
.about-band{position:absolute;left:0;top:1183px;width:1200px;height:376px;background:linear-gradient(100deg,#3c4650 0%,#252c33 50%,#161b20 100%)}
.about-card{position:absolute;left:238px;top:1398px;width:718px;height:312px;background:var(--white);border:1px solid #e5e5e5;text-align:center;padding:30px 72px 0}
.about-card .eyebrow{font-size:17px;color:var(--ink)}
.about-card h2{font-size:28px;font-weight:600;color:var(--heading);margin:4px 0 18px}
.about-card p{font-size:12.5px;line-height:19.5px;color:var(--text);margin-bottom:10px}

/* services */
.service{position:absolute;top:1853px;width:204px;text-align:center}
.service-photo{width:204px;height:204px}
.service h4{margin-top:14px;font-size:15px;font-weight:600;line-height:21px;color:var(--heading)}

/* contact */
.contact{position:absolute;left:0;top:2190px;width:1200px;height:472px;background:var(--light-bg)}
.contact h2{position:absolute;font-size:28px;font-weight:600;color:var(--heading)}
.divider{position:absolute;left:366px;top:75px;width:1px;height:305px;background:#cfd4d8}
.info-label{position:absolute;left:98px;font-size:15px;font-weight:600;color:var(--ink)}
.info-icon{position:absolute;left:60px}
.info-text{position:absolute;left:61px;font-size:13px;line-height:21px;color:var(--text)}
.field{position:absolute;border-bottom:1px solid #b9bfc4;font-size:12.5px;color:#555}
.field.strong{color:var(--ink);font-weight:500;border-bottom-color:#556}
.send-btn{position:absolute;left:419px;top:2546px;width:160px;height:40px;background:var(--red);color:var(--white);font-size:15px;font-weight:600;display:flex;align-items:center;justify-content:center}
.send-btn::after{content:"";position:absolute;right:-12px;top:0;width:6px;height:100%;background:var(--red)}

/* footer */
.site-footer{position:absolute;left:0;top:2662px;width:1200px;height:293px;background:var(--navy);color:var(--white);text-align:center}
.footer-brand{position:absolute;left:0;width:1200px;top:56px;display:flex;justify-content:center;align-items:center;gap:10px;font-size:32px;font-weight:600}
.footer-contact{position:absolute;left:0;width:1200px;top:142px;display:flex;justify-content:center;align-items:center;font-size:13px}
.footer-contact .sep{width:1px;height:26px;background:#6b7b88;margin:0 24px}
.footer-links{position:absolute;left:0;width:1200px;top:200px;font-size:13px}
.footer-copy{position:absolute;left:0;width:1200px;top:226px;font-size:13px}
</style>
</head>
<body>

<section class="hero" role="img" aria-label="Photo of a technician holding a tablet in a server room"></section>

<header class="site-header">
  <div class="brand"><span class="brand-mark"></span>Brivano Systems</div>
  <nav class="main-nav">
    <a class="active" href="#">Home</a><a href="#">About Us</a><a href="#">Services</a><a href="#">Contact Us</a>
  </nav>
  <div class="call-btn" style="left:953px;top:21px">
    <svg width="22" height="22" viewBox="0 0 24 24"><path fill="#fff" d="M6.6 10.8a15.1 15.1 0 0 0 6.6 6.6l2.2-2.2a1 1 0 0 1 1-.25 11.4 11.4 0 0 0 3.6.57 1 1 0 0 1 1 1V20a1 1 0 0 1-1 1A17 17 0 0 1 3 4a1 1 0 0 1 1-1h3.5a1 1 0 0 1 1 1c0 1.25.2 2.45.57 3.6a1 1 0 0 1-.25 1z"/></svg>
    555-014-2280
  </div>
</header>

<h1 class="hero-title">Data Center</h1>
<div class="hero-rule"></div>
<div class="hero-sub">Services</div>
<p class="hero-text">We offer colocation, virtualization, storage as a service and disaster recovery out of our own enterprise-grade data center.</p>
<div class="call-btn" style="left:60px;top:460px">
  <svg width="22" height="22" viewBox="0 0 24 24"><path fill="#fff" d="M6.6 10.8a15.1 15.1 0 0 0 6.6 6.6l2.2-2.2a1 1 0 0 1 1-.25 11.4 11.4 0 0 0 3.6.57 1 1 0 0 1 1 1V20a1 1 0 0 1-1 1A17 17 0 0 1 3 4a1 1 0 0 1 1-1h3.5a1 1 0 0 1 1 1c0 1.25.2 2.45.57 3.6a1 1 0 0 1-.25 1z"/></svg>
  555-014-2280
</div>

<h2 class="section-title" style="top:748px">Why Choose Us</h2>
<div class="link-line" style="left:420px;width:67px"></div>
<div class="link-line" style="left:714px;width:67px"></div>

<div class="feature" style="left:193px;top:830px">
  <svg width="60" height="50" viewBox="0 0 60 50" fill="none" stroke="#c8262f" stroke-width="2"><path d="M4 18l10-8 10 4 8-4 10 2 14 6"/><path d="M4 18l16 18 6 4 6-2 14-14 10-6"/><path d="M22 28l6 6M28 24l6 6M34 20l6 6"/></svg>
  <h3>A True Partner</h3>
  <p>One size data center architecture does not fit all. We take the time to understand your specific requirements.</p>
</div>
<div class="feature" style="left:487px;top:883px">
  <svg width="44" height="50" viewBox="0 0 44 50" fill="none" stroke="#c8262f" stroke-width="2"><path d="M22 3l17 6v14c0 12-8 20-17 24C13 43 5 35 5 23V9z"/><circle cx="22" cy="21" r="7"/><path d="M18 28l-3 9 7-3 7 3-3-9"/></svg>
  <h3>High Security</h3>
  <p>Our data center is a Tier III, standalone structure designed to withstand wind speeds up to 206mph.</p>
</div>
<div class="feature" style="left:780px;top:830px">
  <svg width="52" height="50" viewBox="0 0 52 50" fill="none" stroke="#c8262f" stroke-width="2"><ellipse cx="26" cy="8" rx="7" ry="3"/><path d="M19 8v8c0 2 14 2 14 0V8"/><circle cx="35" cy="20" r="6"/><path d="M32 20l2 2 4-4"/><path d="M4 34h8l10 4h10l14-8-4-2-12 5H22"/><path d="M4 42h10l14 4 20-12"/></svg>
  <h3>Availability</h3>
  <p>The facility is powered by two separate utility feeds and a Tremont diesel generator.</p>
</div>

<div class="about-band" role="img" aria-label="Photo of two engineers working at computer monitors"></div>
<div class="about-card">
  <div class="eyebrow">About</div>
  <h2>Brivano Systems</h2>
  <p>Like most great businesses Brivano Systems began in a garage during the summer of 1995 in Maple Falls, SC. It was a part time venture by Marcus Delane and his business partner Owen Trask. They had discovered an opportunity in technology sales and service after a combined 30 years at Harlow Power in information technology.</p>
  <p>Today, the company has grown significantly and continues to do so. Brivano Systems provides services including multi-dwelling unit managed networks, data center services, low voltage wiring and local office IT support. Industries served include: retail, manufacturing, MDUs, hospitality, software development, medical, construction and more.</p>
</div>

<h2 class="section-title" style="top:1782px">Our Services</h2>
<div class="service" style="left:60px"><div class="service-photo" role="img" aria-label="Photo of hands typing with security icons overlay" style="background:linear-gradient(135deg,#2b4a6e,#0f1e33)"></div><h4>Managed<br>Cybersecurity</h4></div>
<div class="service" style="left:279px"><div class="service-photo" role="img" aria-label="Photo of an engineer with a laptop between server racks" style="background:linear-gradient(135deg,#1d1f22,#4a4c50)"></div><h4>Managed Networks<br>for MDUs</h4></div>
<div class="service" style="left:498px"><div class="service-photo" role="img" aria-label="Photo of an operator at monitors in a data center" style="background:linear-gradient(135deg,#1b3858,#0c1a2c)"></div><h4>Data Center<br>Services</h4></div>
<div class="service" style="left:717px"><div class="service-photo" role="img" aria-label="Photo of hands wiring a low voltage wall box" style="background:linear-gradient(135deg,#aebfd2,#7f95ad)"></div><h4>Low Voltage<br>Wiring</h4></div>
<div class="service" style="left:936px"><div class="service-photo" role="img" aria-label="Photo of two colleagues at an office workstation" style="background:linear-gradient(135deg,#d9dfe4,#5e666e)"></div><h4>Office IT<br>Support</h4></div>

<section class="contact">
  <h2 style="left:61px;top:72px">Contact Us</h2>
  <h2 style="left:412px;top:72px">Get In Touch</h2>
  <div class="divider"></div>

  <svg class="info-icon" style="top:138px" width="20" height="20" viewBox="0 0 24 24"><path fill="#c8262f" d="M6.6 10.8a15.1 15.1 0 0 0 6.6 6.6l2.2-2.2a1 1 0 0 1 1-.25 11.4 11.4 0 0 0 3.6.57 1 1 0 0 1 1 1V20a1 1 0 0 1-1 1A17 17 0 0 1 3 4a1 1 0 0 1 1-1h3.5a1 1 0 0 1 1 1c0 1.25.2 2.45.57 3.6a1 1 0 0 1-.25 1z"/></svg>
  <div class="info-label" style="top:138px">Call Us</div>
  <div class="info-text" style="top:168px">555-014-2280.</div>

  <svg class="info-icon" style="top:218px" width="20" height="16" viewBox="0 0 20 16"><rect x="1" y="1" width="18" height="14" fill="#c8262f"/><path d="M1 1l9 8 9-8M1 15l7-7M19 15l-7-7" stroke="#fff" stroke-width="1.5" fill="none"/></svg>
  <div class="info-label" style="top:214px">Email</div>
  <div class="info-text" style="top:245px">support@brivanoqe.com</div>

  <svg class="info-icon" style="top:293px" width="16" height="20" viewBox="0 0 16 20"><path fill="#c8262f" d="M8 0a7 7 0 0 1 7 7c0 5-7 13-7 13S1 12 1 7a7 7 0 0 1 7-7z"/><circle cx="8" cy="7" r="2.6" fill="#e9edf0"/></svg>
  <div class="info-label" style="top:293px">Location</div>
  <div class="info-text" style="top:325px">Brivano Systems 48 Ridgeline Parkway<br>Maple Falls, SC 29000</div>

  <div class="field strong" style="left:419px;top:148px;width:336px;height:44px">First Name</div>
  <div class="field" style="left:795px;top:148px;width:336px;height:44px">Last Name</div>
  <div class="field" style="left:419px;top:208px;width:336px;height:44px">Email</div>
  <div class="field" style="left:795px;top:208px;width:336px;height:44px">Phone Number</div>
  <div class="field" style="left:419px;top:268px;width:712px;height:64px">Message</div>
</section>
<div class="send-btn">Send Message</div>

<footer class="site-footer">
  <div class="footer-brand"><span class="brand-mark"></span>Brivano Systems</div>
  <div class="footer-contact">
    <span><strong style="font-weight:500">Phone No :</strong> 555-014-2280</span>
    <span class="sep"></span>
    <span><strong style="font-weight:500">Email :</strong> support@brivanoqe.com</span>
  </div>
  <div class="footer-links">Home | Services | About | Contact</div>
  <div class="footer-copy">2025 © Brivano Systems of SC, Inc.</div>
</footer>

</body>
</html>
```